Q7 Picks High Quality Stainless Steel Professional Guitar Picks

I am releasing a new line of Guitar Picks.
These picks are made of stainless steel with an innovative design and manufacturing process. These Picks are for electric guitar and bass guitar players with a modern look, feel and tone. I need packaging that looks high quality, professional, with a modern feel. I also want them to look almost like a luxury product, "The Valdrenne of guitar picks" luxury but modern and masculine. The packaging itself should show off the product so potential buyers can see the product from inside the packaging while not taking up much retail space when displayed. each package will include a qty of 4 Picks. would be great for product to be seen from the front and back. not closed in a box unless the box has windows for the picks viewable from both sides.

Target Market(s)

Musicians, Electric Bass and guitar players all Genre's of music. all ages, professionals. and semi professionals.

Industry/Entity Type

Steel

Font styles to use
Serif
Sans Serif
Other font styles liked:
• Bank Gothic

Colors

Designer to choose colors to be used in the design.

Requirements
Must have
• packaging to be simple I don't want my cost of packaging to be expensive to produce. If you google guitar pick packaging its very simple its just a small polly bag with a header card stapled over it and it hangs on retail hooks. I want something similar but still unique. I am open to other ideas than the typical hang tag/polybag.
Nice to have
• Just to explain a little further "hopefully this is making sense."
• Starting out I plan on having 3 different size picks with matching packaging plus a sample pack. The different Picks are labeled as
• Standard, Jazz, & Bass.
• Standard picks have a black finish with Orange logo.
• "PMS 151 C" (packaging to match.)
• Jazz picks have a Copper finish with a Silver Logo.
• (packaging to match.)
• Bass picks have a Gun Metal finish with a Teal logo
• "PMS 7465 C" (packaging to match.)
• Sample pack will contain 3 Picks (one of each)
• packaging colors TBD.
Should not have
• a picture or drawing of the product, music notes, pictures or drawings of guitars

```html
<!DOCTYPE html>
<html lang="en">
<head>
<meta charset="utf-8">
<title>Q7 Picks – Header Card</title>
<link rel="stylesheet" href="https://fonts.googleapis.com/css2?family=Michroma&family=Saira:wght@400;500&display=swap">
<style>
  :root {
    --stage: #eef1ea;
    --card-white: #ffffff;
    --card-black: #111314;
    --brand-orange: #e2690f;
    --band-brown: #4a2410;
    --line-grey: #a9a9a9;
    --text-white: #ffffff;
    --text-silver: #d7dcdc;
    --badge-red: #b3121a;
  }
  html, body {
    margin: 0;
    width: 1200px;
    height: 1200px;
    overflow: hidden;
    background: var(--stage);
  }
  .canvas {
    position: relative;
    width: 1200px;
    height: 1200px;
  }
  .header-card {
    position: absolute;
    left: 100px;
    top: 190px;
    width: 1000px;
    height: 820px;
    background: var(--card-white);
    box-shadow: 0 6px 24px rgba(0,0,0,0.18);
    overflow: hidden;
  }
  .card-art {
    position: absolute;
    inset: 0;
    width: 1000px;
    height: 820px;
  }
  .qty-badge {
    position: absolute;
    left: 80px;
    top: 70px;
    width: 130px;
    text-align: center;
  }
  .qty-badge__circle {
    width: 84px;
    height: 84px;
    margin: 0 auto;
    border-radius: 50%;
    background: var(--badge-red);
    border: 5px solid var(--card-black);
    box-sizing: border-box;
    color: var(--text-white);
    font-family: "Michroma", sans-serif;
    font-size: 44px;
    line-height: 74px;
  }
  .qty-badge__label {
    display: inline-block;
    margin-top: -10px;
    position: relative;
    background: var(--card-black);
    color: var(--text-white);
    font-family: "Michroma", sans-serif;
    font-size: 22px;
    padding: 2px 8px;
  }
  .product-line {
    position: absolute;
    left: 340px;
    top: 230px;
    margin: 0;
    color: var(--text-white);
    font-family: "Saira", sans-serif;
    font-weight: 400;
    font-size: 52px;
    letter-spacing: 0.5px;
  }
  .brand-name {
    position: absolute;
    left: 330px;
    top: 330px;
    margin: 0;
    color: var(--brand-orange);
    font-family: "Michroma", sans-serif;
    font-weight: 400;
    font-size: 100px;
    line-height: 1;
  }
  .tagline {
    position: absolute;
    left: 330px;
    top: 688px;
    margin: 0;
    color: var(--text-white);
    font-family: "Michroma", sans-serif;
    font-size: 40px;
    line-height: 58px;
    letter-spacing: 1px;
  }
  .tagline span { display: block; }
  .tagline .tagline__second { padding-left: 0; }
</style>
</head>
<body>
<main class="canvas">
  <section class="header-card" aria-label="Q7 Picks header card">
    <svg class="card-art" viewBox="0 0 1000 820" aria-hidden="true">
      <defs>
        <linearGradient id="arcEdge" x1="0" y1="0" x2="0" y2="1">
          <stop offset="0" stop-color="#c8651a"/>
          <stop offset="1" stop-color="#9a9a98"/>
        </linearGradient>
        <linearGradient id="bandFill" x1="0" y1="0" x2="1" y2="0">
          <stop offset="0" stop-color="#e2690f"/>
          <stop offset="0.55" stop-color="#6a3210"/>
          <stop offset="1" stop-color="#1a1410"/>
        </linearGradient>
      </defs>
      <!-- curved dark panel -->
      <path class="panel-edge" d="M 585 0 L 1000 0 L 1000 820 L 150 820 A 770 770 0 0 1 585 0 Z" fill="url(#arcEdge)"/>
      <path class="panel-dark" d="M 610 0 L 1000 0 L 1000 820 L 172 820 A 750 750 0 0 1 610 0 Z" fill="var(--card-black)"/>
      <!-- bottom band -->
      <rect class="bottom-band" x="0" y="660" width="1000" height="160" fill="url(#bandFill)"/>
      <!-- string lines, left -->
      <g stroke="var(--line-grey)" stroke-width="2">
        <line x1="20" y1="705" x2="250" y2="705"/>
        <line x1="20" y1="720" x2="250" y2="720"/>
        <line x1="20" y1="735" x2="250" y2="735"/>
        <line x1="20" y1="750" x2="250" y2="750"/>
        <line x1="20" y1="765" x2="250" y2="765"/>
      </g>
      <!-- string lines, right -->
      <g stroke="var(--line-grey)" stroke-width="2">
        <line x1="770" y1="640" x2="990" y2="640"/>
        <line x1="770" y1="655" x2="990" y2="655"/>
        <line x1="770" y1="670" x2="990" y2="670"/>
        <line x1="770" y1="685" x2="990" y2="685"/>
        <line x1="770" y1="700" x2="990" y2="700"/>
      </g>
      <!-- hang hole -->
      <path class="hang-hole" d="M 455 95 L 490 95 Q 495 75 520 75 Q 545 75 550 95 L 580 95 Q 595 95 595 110 Q 595 125 580 125 L 455 125 Q 440 125 440 110 Q 440 95 455 95 Z" fill="none" stroke="#e8e8e8" stroke-width="2"/>
    </svg>

    <div class="qty-badge">
      <div class="qty-badge__circle">4</div>
      <div class="qty-badge__label">PICKS</div>
    </div>

    <p class="product-line">Stainless Steel</p>
    <h1 class="brand-name">Q7 Picks</h1>

    <p class="tagline">
      <span>TONE IS NOW</span>
      <span class="tagline__second">IN YOUR HAND</span>
    </p>
  </section>
</main>
</body>
</html>
```